Redesign of our homepage

We are a company that operates in the Wellness tourism sector. We are starting a project to redesign our homepage. See the screenshots. The main idea is that the banner image and the text on the banner are dynamically replaced depending on whether a user clicks on the "Thumb up" or the "Thumb down" icon.
You can see a live version of our homepage at http://demo.velqorambe.com

Requirements
Must have
• Must abide by style and look & feel of the current site.
It is important to demonstrate the functionality that enables the banner image and text being refreshed at each click of a ThumbUp or ThumbDown icons. In others words the Javascript must work.

Let me add some more context on the project.

Actually the thumb up and thumb down are possible answers to question/comment dynamically displayed at the location of the current text "Experience That Make You tell an unforgettable story".
An example of a comment/question is "I need a program that would help limit my stress levels and make me look great and feel fantastic". Or "I need an activity that will reduce my stress."
So a user would have to click on a thumb up or thumb down to approve or disapprove these questions/comments..
Based on this information, I think you could move the thumbs up to the left and right side of the text (the comment/question) respectively. And move the reset underneath in the middle.

Maybe it's a good idea to reduce the font size of that text as well.

And now to the dropdown list. We need only 2 of them, and not 3 as you have displayed.
One of them contain the list:
-- I need a weekend retreat
-- ! need a week or more retreat
The other would contain a list of countries.
The drop down values must be selected before the thumbs up and down thumbs are active.
Therefore you should move them above the question/comment text.
And finally about the thumbs and reset icons. Please put them in a round orange color and make them a bit bigger.

```html
<!DOCTYPE html>
<html lang="en">
<head>
<meta charset="utf-8">
<title>Velqorambe – Homepage Redesign</title>
<link rel="stylesheet" href="https://fonts.googleapis.com/css2?family=Lato:wght@400;700&family=Oswald:wght@300;700&display=swap">
<style>
  :root{
    --stage:#ebebeb;
    --ink:#ffffff;
    --ink-soft:#d9dde0;
    --dark:#0b0e11;
    --mist:#e3e3e3;
    --slate:#56636d;
    --orange:#f0922f;
    --grey-btn:#8c8c8c;
    --pill:rgba(235,235,235,.88);
    --pill-text:#2a2a2a;
  }
  *{box-sizing:border-box;margin:0;padding:0}
  html,body{width:1200px;height:1200px;overflow:hidden;background:var(--stage)}
  body{position:relative;font-family:'Lato',sans-serif;color:var(--ink)}

  /* ---------- Hero screen ---------- */
  .hero-screen{position:absolute;left:336px;top:597px;width:832px;height:603px;overflow:hidden}
  .hero-photo{position:absolute;inset:0;
    background:
      linear-gradient(180deg,rgba(255,255,255,.92) 0%,rgba(240,240,238,.6) 12%,rgba(0,0,0,0) 30%),
      radial-gradient(ellipse 40% 55% at 48% 68%,#5a3a2a 0%,rgba(90,58,42,0) 100%),
      linear-gradient(180deg,#8f9a86 0%,#6d6450 35%,#8a6a4a 55%,#c9a77a 78%,#d8bf95 100%)}
  .hero-nav{position:absolute;top:34px;right:108px;display:flex;align-items:center;gap:20px}
  .hero-nav .nav-link{font-size:9px;color:#1e1e1e;letter-spacing:.3px}
  .hero-nav .nav-cut{margin-right:-4px}
  .sign-in{width:64px;height:17px;border-radius:9px;background:var(--orange);color:#fff;font-size:9px;font-weight:700;display:flex;align-items:center;justify-content:center;letter-spacing:.3px}
  .social-rail{position:absolute;left:159px;top:168px;display:flex;flex-direction:column;gap:18px}
  .social-rail span{width:8px;height:8px;border-radius:50%;background:#fff;display:block}
  .picker{position:absolute;top:222px;height:22px;width:182px;border-radius:11px;background:var(--pill);display:flex;align-items:center;padding:0 10px 0 9px;gap:6px;font-size:7px;color:var(--pill-text)}
  .picker-retreat{left:227px}
  .picker-country{left:420px}
  .picker .label{flex:1}
  .picker svg{flex:none}
  .tagline{position:absolute;left:500px;top:268px;font-family:'Oswald',sans-serif;color:#fff}
  .tagline .lead{font-weight:300;font-size:25px;line-height:1}
  .tagline .wild{font-weight:700;font-size:82px;line-height:.9;letter-spacing:-1px;margin-top:4px}
  .vote{position:absolute;top:382px;width:34px;height:34px;border-radius:50%;background:var(--orange);display:flex;align-items:center;justify-content:center;box-shadow:0 2px 6px rgba(0,0,0,.25)}
  .vote-up{left:483px}
  .vote-reset{left:569px;background:var(--grey-btn)}
  .vote-down{left:654px}

  /* ---------- Listing + footer screen ---------- */
  .listing-screen{position:absolute;left:22px;top:0;width:876px;height:694px;overflow:hidden;background:var(--dark)}
  .landscape{position:absolute;inset:0;
    background:
      radial-gradient(ellipse 22% 16% at 10% 26%,rgba(255,255,255,.95) 0%,rgba(255,255,255,0) 100%),
      linear-gradient(180deg,var(--mist) 0%,#d8d8d8 28%,#7c8790 36%,var(--slate) 44%,#2d363d 56%,#161b20 68%,var(--dark) 80%)}
  .tour-card{position:absolute;width:184px;border-radius:25px;overflow:hidden;box-shadow:0 4px 10px rgba(0,0,0,.35);display:flex;flex-direction:column;justify-content:flex-end;padding:0 12px 8px 13px}
  .tour-photo{position:absolute;inset:0;z-index:0}
  .tour-card > *:not(.tour-photo){position:relative;z-index:1}
  .card-coast{left:145px;top:-60px;height:185px}
  .card-coast .tour-photo{background:linear-gradient(180deg,#6b5146 0%,#544640 55%,#3c3634 100%)}
  .card-giraffe{left:347px;top:-30px;height:259px}
  .card-giraffe .tour-photo{background:linear-gradient(160deg,#8e8a82 0%,#6f6a60 45%,#3f5448 80%,#2e4438 100%)}
  .card-road{left:548px;top:-40px;height:214px}
  .card-road .tour-photo{background:linear-gradient(180deg,#2a2d2a 0%,#3a3f36 50%,#4b4d48 80%,#2b2b2b 100%)}
  .tour-title{font-size:15.5px;font-weight:700;line-height:19px;letter-spacing:.4px;margin-bottom:6px}
  .tour-facts{list-style:none;font-size:11px;line-height:19px;letter-spacing:.3px;color:var(--ink-soft)}
  .tour-facts li{display:flex;align-items:center;gap:6px}
  .tour-price{font-size:20.5px;font-weight:700;text-align:right;margin-top:6px;letter-spacing:.5px;padding-right:6px}

  .site-footer{position:absolute;left:146px;top:486px;display:flex;gap:0}
  .footer-col{width:121px}
  .footer-col h3{font-size:9.5px;font-weight:700;letter-spacing:.6px;padding-bottom:7px;border-bottom:1px solid rgba(255,255,255,.7);width:81px;white-space:nowrap}
  .footer-col p,.footer-col li{font-size:7.7px;line-height:11.4px;letter-spacing:.3px;color:var(--ink-soft);list-style:none}
  .footer-col .body{margin-top:18px}
  .footer-col.legal p{width:105px}
  .copyright{position:absolute;left:0;width:100%;top:646px;text-align:center;font-size:8px;letter-spacing:.4px;color:var(--ink-soft)}
  .footer-social{position:absolute;left:0;width:100%;top:664px;display:flex;justify-content:center;gap:19px}
  .footer-social span{width:8px;height:8px;border-radius:50%;background:#fff;display:block}
</style>
</head>
<body>

<section class="hero-screen" aria-label="Homepage hero">
  <div class="hero-photo" role="img" aria-label="Red deer stag with large antlers standing in golden grass before autumn trees"></div>
  <nav class="hero-nav">
    <span class="nav-link nav-cut">e</span>
    <span class="nav-link">Partners</span>
    <span class="sign-in">Sign In</span>
  </nav>
  <div class="social-rail" aria-label="Social links"><span></span><span></span><span></span><span></span></div>

  <div class="picker picker-retreat">
    <svg width="12" height="9" viewBox="0 0 12 9"><path d="M6 1 C4.5 3 4.5 6 6 8 C7.5 6 7.5 3 6 1Z M1 4 C2 7 4 8 6 8 C4 6 2.5 5 1 4Z M11 4 C10 7 8 8 6 8 C8 6 9.5 5 11 4Z" fill="#333"/></svg>
    <span class="label">I need a weekend retreat</span>
    <svg width="7" height="5" viewBox="0 0 7 5"><path d="M1 1 L3.5 3.5 L6 1" fill="none" stroke="#333" stroke-width="1.2"/></svg>
  </div>
  <div class="picker picker-country">
    <svg width="12" height="12" viewBox="0 0 12 12"><circle cx="6" cy="6" r="5" fill="none" stroke="#333" stroke-width="1"/><ellipse cx="6" cy="6" rx="2.2" ry="5" fill="none" stroke="#333" stroke-width=".8"/><path d="M1 6 H11 M2 3.5 H10 M2 8.5 H10" stroke="#333" stroke-width=".8"/></svg>
    <span class="label">Countries</span>
    <svg width="7" height="5" viewBox="0 0 7 5"><path d="M1 1 L3.5 3.5 L6 1" fill="none" stroke="#333" stroke-width="1.2"/></svg>
  </div>

  <div class="tagline">
    <div class="lead">step in to the</div>
    <div class="wild">WILD?</div>
  </div>

  <div class="vote vote-up" aria-label="Thumb up">
    <svg width="16" height="16" viewBox="0 0 16 16"><rect x="1" y="7" width="3" height="8" rx=".5" fill="#fff"/><path d="M5 7 L8 2 C9 1 10.5 1.8 10 3.2 L9.3 6 H13.5 C14.5 6 15.2 7 14.9 8 L13.6 13.8 C13.4 14.5 12.8 15 12 15 H5 Z" fill="#fff"/></svg>
  </div>
  <div class="vote vote-reset" aria-label="Reset">
    <svg width="16" height="16" viewBox="0 0 16 16"><path d="M4.2 5 A5 5 0 1 0 8 3" fill="none" stroke="#fff" stroke-width="1.7" stroke-linecap="round"/><path d="M8 0.5 L8 5.5 L4.5 3 Z" fill="#fff"/></svg>
  </div>
  <div class="vote vote-down" aria-label="Thumb down">
    <svg width="16" height="16" viewBox="0 0 16 16"><g transform="rotate(180 8 8)"><rect x="1" y="7" width="3" height="8" rx=".5" fill="#fff"/><path d="M5 7 L8 2 C9 1 10.5 1.8 10 3.2 L9.3 6 H13.5 C14.5 6 15.2 7 14.9 8 L13.6 13.8 C13.4 14.5 12.8 15 12 15 H5 Z" fill="#fff"/></g></svg>
  </div>
</section>

<section class="listing-screen" aria-label="Tours and footer">
  <div class="landscape" role="img" aria-label="Misty mountain range with dark pine forest and drifting clouds"></div>

  <article class="tour-card card-coast">
    <div class="tour-photo" role="img" aria-label="Coastal tour photo"></div>
    <ul class="tour-facts">
      <li><svg width="9" height="9" viewBox="0 0 9 9"><rect x=".5" y="1.5" width="8" height="7" fill="#fff"/><rect x="1.5" y="3.5" width="6" height="4" fill="#5a4a44"/><rect x="2" y="0" width="1" height="2" fill="#fff"/><rect x="6" y="0" width="1" height="2" fill="#fff"/></svg>3 days / 2 nights</li>
      <li><svg width="9" height="9" viewBox="0 0 9 9"><circle cx="4.5" cy="2.5" r="2.3" fill="#fff"/><path d="M0.5 9 C0.5 6 2.5 5 4.5 5 C6.5 5 8.5 6 8.5 9 Z" fill="#fff"/></svg>Minimum no. of persons: 1</li>
      <li><svg width="9" height="9" viewBox="0 0 9 9"><circle cx="4.5" cy="2.5" r="2.3" fill="#fff"/><path d="M0.5 9 C0.5 6 2.5 5 4.5 5 C6.5 5 8.5 6 8.5 9 Z" fill="#fff"/></svg>Maximum group size: 8</li>
      <li><svg width="9" height="9" viewBox="0 0 9 9"><circle cx="4.5" cy="2.5" r="2.3" fill="#fff"/><path d="M0.5 9 C0.5 6 2.5 5 4.5 5 C6.5 5 8.5 6 8.5 9 Z" fill="#fff"/></svg>Minimum age: 10 years</li>
    </ul>
    <div class="tour-price">$190.00</div>
  </article>

  <article class="tour-card card-giraffe">
    <div class="tour-photo" role="img" aria-label="Giraffe tour photo"></div>
    <h2 class="tour-title">3 Days Big Five<br>Tented Safari,<br>Kruger National Park,<br>South Africa</h2>
    <ul class="tour-facts">
      <li><svg width="9" height="9" viewBox="0 0 9 9"><rect x=".5" y="1.5" width="8" height="7" fill="#fff"/><rect x="1.5" y="3.5" width="6" height="4" fill="#6f6a60"/><rect x="2" y="0" width="1" height="2" fill="#fff"/><rect x="6" y="0" width="1" height="2" fill="#fff"/></svg>3 days / 2 nights</li>
      <li><svg width="9" height="9" viewBox="0 0 9 9"><circle cx="4.5" cy="2.5" r="2.3" fill="#fff"/><path d="M0.5 9 C0.5 6 2.5 5 4.5 5 C6.5 5 8.5 6 8.5 9 Z" fill="#fff"/></svg>Minimum no. of persons: 1</li>
      <li><svg width="9" height="9" viewBox="0 0 9 9"><circle cx="4.5" cy="2.5" r="2.3" fill="#fff"/><path d="M0.5 9 C0.5 6 2.5 5 4.5 5 C6.5 5 8.5 6 8.5 9 Z" fill="#fff"/></svg>Maximum group size: 8</li>
      <li><svg width="9" height="9" viewBox="0 0 9 9"><circle cx="4.5" cy="2.5" r="2.3" fill="#fff"/><path d="M0.5 9 C0.5 6 2.5 5 4.5 5 C6.5 5 8.5 6 8.5 9 Z" fill="#fff"/></svg>Minimum age: 10 years</li>
    </ul>
    <div class="tour-price">$420.00</div>
  </article>

  <article class="tour-card card-road">
    <div class="tour-photo" role="img" aria-label="Countryside road tour photo"></div>
    <h2 class="tour-title">3 Days Masai Mara<br>And Lake Nakuru<br>Safari Tour<br>In Kenya</h2>
    <ul class="tour-facts">
      <li><svg width="9" height="9" viewBox="0 0 9 9"><rect x=".5" y="1.5" width="8" height="7" fill="#fff"/><rect x="1.5" y="3.5" width="6" height="4" fill="#3a3f36"/><rect x="2" y="0" width="1" height="2" fill="#fff"/><rect x="6" y="0" width="1" height="2" fill="#fff"/></svg>3 days / 2 nights</li>
      <li><svg width="9" height="9" viewBox="0 0 9 9"><circle cx="4.5" cy="2.5" r="2.3" fill="#fff"/><path d="M0.5 9 C0.5 6 2.5 5 4.5 5 C6.5 5 8.5 6 8.5 9 Z" fill="#fff"/></svg>Minimum no. of persons: 1</li>
      <li><svg width="9" height="9" viewBox="0 0 9 9"><circle cx="4.5" cy="2.5" r="2.3" fill="#fff"/><path d="M0.5 9 C0.5 6 2.5 5 4.5 5 C6.5 5 8.5 6 8.5 9 Z" fill="#fff"/></svg>Maximum group size: 8</li>
      <li><svg width="9" height="9" viewBox="0 0 9 9"><circle cx="4.5" cy="2.5" r="2.3" fill="#fff"/><path d="M0.5 9 C0.5 6 2.5 5 4.5 5 C6.5 5 8.5 6 8.5 9 Z" fill="#fff"/></svg>Minimum age: 10 years</li>
    </ul>
    <div class="tour-price">$280.00</div>
  </article>

  <footer>
    <div class="site-footer">
      <div class="footer-col legal">
        <h3>LEGAL INFOMATION</h3>
        <div class="body"><p>VELQORAMBE B.V. is registered with the trade register of the Chamber of Commerce in Utrecht, the Netherlands, under registration number 58213094.<br>VAT registration number is NL472093816B02.</p></div>
      </div>
      <div class="footer-col">
        <h3>VELQORAMBE</h3>
        <ul class="body"><li>About Us</li><li>Contact Us</li><li>Terms and Conditions</li><li>Privacy</li></ul>
      </div>
      <div class="footer-col">
        <h3>SUSTAINABILITY</h3>
        <ul class="body"><li>Our Climate Pledge</li><li>Our Progress</li><li>How It Works</li></ul>
      </div>
      <div class="footer-col">
        <h3>OUR PARTNERS</h3>
        <ul class="body"><li>Organizers</li><li>Rootfund.org</li></ul>
      </div>
      <div class="footer-col">
        <h3>CONTACT</h3>
        <ul class="body"><li>Leiden, the</li><li>Netherlands</li><li>info@velqorambe.com</li><li>+ 01 987 654 32</li></ul>
      </div>
    </div>
    <p class="copyright">© 2020 VELQORAMBE B.V.</p>
    <div class="footer-social" aria-label="Social links"><span></span><span></span><span></span><span></span></div>
  </footer>
</section>

</body>
</html>
```